Lantern Stewardship Frame

I am looking for a graphic design of the attached leadership model. The colors and design can be altered in any manner that brings the model alive version of the house model.

```html
<!DOCTYPE html>
<html lang="en">
<head>
<meta charset="utf-8">
<title>Lantern Stewardship Frame</title>
<link href="https://fonts.googleapis.com/css2?family=Barlow:wght@400;500;700&display=swap" rel="stylesheet">
<style>
  :root{
    --bg:#eef7fc;
    --panel:#ffffff;
    --field:#f1f2f4;
    --red:#f40a0a;
    --navy:#233f7d;
    --ink:#1d2c55;
    --blue:#05aeea;
    --orange:#ff6a00;
    --green:#8ed14f;
    --slate:#8597b1;
    --sky1:#bfe3f5;
    --sky2:#7ec5ea;
  }
  *{box-sizing:border-box;margin:0;padding:0}
  html,body{width:1200px;height:675px;overflow:hidden}
  body{position:relative;background:linear-gradient(135deg,#f4fafd,var(--bg));font-family:"Barlow",Arial,sans-serif;color:var(--ink)}
  .abs{position:absolute}
  .brand-tab{left:0;top:52px;width:234px;height:79px;background:var(--red);border-radius:0 12px 12px 0;color:#fff;font-weight:700;font-size:30px;letter-spacing:.5px;display:flex;align-items:center;justify-content:center;padding-left:18px}
  .mission{left:20px;top:166px;width:222px;text-align:center;font-size:25px;line-height:30px;color:var(--navy);font-weight:500;text-transform:uppercase}
  .hero-art{left:0;top:456px;width:256px;height:219px;background:linear-gradient(160deg,var(--sky1) 0%,var(--sky2) 70%,#5fb3e0 100%);border-radius:0 140px 0 0;clip-path:polygon(0 22%,40% 10%,100% 0,60% 40%,35% 75%,25% 100%,0 100%)}
  .board{left:274px;top:51px;width:960px;height:583px;background:var(--panel);border-radius:31px 0 0 31px}
  .board-title{left:298px;top:78px;font-size:24px;font-weight:700;color:var(--navy);letter-spacing:.3px}
  .field{left:294px;top:119px;width:920px;height:369px;background:var(--field);border-radius:25px 0 0 25px}
  .col-head{height:58px;border-radius:6px;color:#fff;padding:13px 0 0 17px;line-height:18px}
  .col-head b{display:block;font-size:14.5px;font-weight:700;letter-spacing:.2px}
  .col-head span{font-size:14px}
  .col-head.org{left:306px;top:147px;width:265px;background:var(--blue)}
  .col-head.inter{left:623px;top:147px;width:251px;background:var(--orange);padding-left:43px}
  .col-head.pers{left:929px;top:147px;width:225px;background:var(--green);padding-left:43px}
  .col-head svg{position:absolute;left:9px;top:11px}
  .item{background:#fff;border-radius:6px;box-shadow:0 3px 8px rgba(30,50,90,.07);font-size:12px;line-height:15px;letter-spacing:.2px;display:flex;align-items:center;padding-left:12px}
  .item::after{content:"";position:absolute;top:50%;width:28px;height:28px;margin-top:-14px;border-radius:50%;border:4.5px solid var(--ring);right:8px;background:#fff}
  .item.org{--ring:var(--blue);left:306px;width:265px;height:45px}
  .item.inter{--ring:var(--orange);left:623px;width:251px;height:45px}
  .item.pers{--ring:var(--green);left:926px;width:228px;height:37px;padding-left:11px}
  .inner-bar{left:294px;top:516px;width:869px;height:33px;background:var(--slate);border-radius:17px;color:#fff;font-size:17.5px;text-align:center;line-height:33px;letter-spacing:.2px}
  .inner{height:33px;background:#fff;border-radius:17px;box-shadow:0 2px 8px rgba(30,50,90,.06);color:var(--navy);font-size:12.5px;letter-spacing:.3px;display:flex;align-items:center;padding-left:13px;gap:6px}
  .inner svg{flex:none}
  .inner.c1{left:291px;width:275px}
  .inner.c2{left:619px;width:266px}
  .inner.c3{left:928px;width:227px}
</style>
</head>
<body>
  <div class="abs brand-tab">LANTERN</div>
  <p class="abs mission">Foster contagious success through people, relationships and a shared vision</p>
  <div class="abs hero-art" role="img" aria-label="Illustration of paper planes flying above soft blue clouds, one red plane leading"></div>

  <div class="abs board"></div>
  <h1 class="abs board-title">OUTER (IMPACT) STRATEGIES</h1>
  <div class="abs field"></div>

  <div class="abs col-head org"><b>ORGANIZATION LEVEL</b><span>WINS THEORY</span></div>
  <div class="abs col-head inter"><svg width="24" height="36" viewBox="0 0 24 36"><polygon points="14,0 24,0 10,18 24,36 14,36 0,18" fill="#ffffff" opacity=".35"/></svg><b>INTERPERSONAL LEVEL</b><span>HEART LISTENING</span></div>
  <div class="abs col-head pers"><svg width="24" height="36" viewBox="0 0 24 36"><polygon points="14,0 24,0 10,18 24,36 14,36 0,18" fill="#ffffff" opacity=".35"/></svg><b>PERSONAL LEVEL</b><span>INSIGHT DIALOGUE</span></div>

  <div class="abs item org" style="top:218px">DEVELOP CONCRETE OUTCOMES,<br>AND VISIBLE RESULTS</div>
  <div class="abs item org" style="top:271px">FOSTER IN-DEPTH CHANGES,<br>AND NEW PRACTICES</div>
  <div class="abs item org" style="top:324px">HAVE A MICRO, INTERPERSONAL<br>OR LOCAL IMPACT</div>
  <div class="abs item org" style="top:378px">CULTIVATE POSITIVE JUDGEMENT,<br>AND SHARED AMBITION</div>

  <div class="abs item inter" style="top:219px">ASK OPEN-ENDED<br>QUESTIONS</div>
  <div class="abs item inter" style="top:272px">AFFIRM SOMEONE’S STRENGTHS,<br>EFFORTS AND PAST SUCCESS</div>
  <div class="abs item inter" style="top:325px">REFLECT BACK WHAT IS SHARED<br>FOR CONFIRMATION</div>
  <div class="abs item inter" style="top:378px">SUMMARIZE KEY POINTS TO<br>GAIN INSIGHTS</div>
  <div class="abs item inter" style="top:431px">SHARE AND DEVELOP<br>MUTUAL EXPERTISE</div>

  <div class="abs item pers" style="top:218px">PAUSE</div>
  <div class="abs item pers" style="top:264px">RELAX</div>
  <div class="abs item pers" style="top:309px">OPEN</div>
  <div class="abs item pers" style="top:354px">ATTUNE TO EMERGENCE</div>
  <div class="abs item pers" style="top:400px">LISTEN DEEPLY</div>
  <div class="abs item pers" style="top:445px">SPEAK THE TRUTH</div>

  <div class="abs inner-bar">INNER (WELLBEING) STRATEGIES</div>

  <div class="abs inner c1" style="top:561px"><svg width="8" height="12" viewBox="0 0 8 12"><path d="M1 0h3l4 6-4 6H1l4-6z" fill="#233f7d"/></svg>PHYSICAL FITNESS</div>
  <div class="abs inner c1" style="top:601px"><svg width="8" height="12" viewBox="0 0 8 12"><path d="M1 0h3l4 6-4 6H1l4-6z" fill="#233f7d"/></svg>NUTRITION</div>
  <div class="abs inner c2" style="top:561px"><svg width="8" height="12" viewBox="0 0 8 12"><path d="M1 0h3l4 6-4 6H1l4-6z" fill="#233f7d"/></svg>HEART RATE VARIABILITY</div>
  <div class="abs inner c2" style="top:601px"><svg width="8" height="12" viewBox="0 0 8 12"><path d="M1 0h3l4 6-4 6H1l4-6z" fill="#233f7d"/></svg>NEUROFEEDBACK</div>
  <div class="abs inner c3" style="top:561px"><svg width="8" height="12" viewBox="0 0 8 12"><path d="M1 0h3l4 6-4 6H1l4-6z" fill="#233f7d"/></svg>ISLAND HOPPIN CLUB</div>
  <div class="abs inner c3" style="top:601px"><svg width="8" height="12" viewBox="0 0 8 12"><path d="M1 0h3l4 6-4 6H1l4-6z" fill="#233f7d"/></svg>VIDEO GAMING CLUB</div>
</body>
</html>
```